Website design for commercial and residential security company

we're looking to see some new designs for an established company with no website.

homepage and one inner page

here is a link to the homepage content, sitemap, logo and more.
https://files.trovelink-share.net/folders/7QmzKpw3RtvxnLa9eHs2YcdJfuoPb?view=open

call to action should be Request A Quote

if you have any questions please send them to us asap

thank you

Number of Pages Required

1 page

Font styles to use
Sans Serif

```html
<!DOCTYPE html>
<html lang="en">
<head>
<meta charset="utf-8">
<title>Sentrafield Security</title>
<link href="https://fonts.googleapis.com/css2?family=Rubik:wght@400;500;700&display=swap" rel="stylesheet">
<style>
:root{
  --yellow:#dea63c;
  --blue:#2f6be3;
  --dark:#1d1e23;
  --darker:#141519;
  --ink:#1f2430;
  --muted:#8a8f99;
  --line:#e7e9ee;
  --white:#ffffff;
}
*{box-sizing:border-box;margin:0;padding:0}
html,body{width:1200px;height:3124px;overflow:hidden}
body{font-family:'Rubik',sans-serif;color:var(--ink);background:var(--white);position:relative}
section,footer{position:absolute;left:0;width:1200px}
.abs{position:absolute}
.label{font-size:10px;letter-spacing:2px;text-transform:uppercase;color:var(--blue);font-weight:500}
.h2{font-size:30px;font-weight:700;line-height:1.25}
.small{font-size:11px;line-height:1.6;color:var(--muted)}
.btn{display:inline-block;font-size:10px;font-weight:500;letter-spacing:1px;text-transform:uppercase;padding:10px 18px;border:1px solid currentColor}

/* hero */
.hero{top:0;height:320px;background:linear-gradient(90deg,#5a6470 0%,#9aa3ad 45%,#e7e9ec 100%)}
.hero-figure{left:600px;top:0;width:360px;height:320px;background:linear-gradient(180deg,#d8dadd,#3f4a66 70%,#e1b43c)}
.hero h1{left:90px;top:-6px;color:var(--white);font-size:50px;font-weight:700;line-height:1.1}
.dots{left:232px;top:284px;display:flex;gap:6px}
.dots span{width:8px;height:8px;border-radius:50%;background:#fff;opacity:.5}
.dots span:first-child{opacity:1;background:var(--dark)}

/* features */
.features{top:320px;height:392px}
.features-intro{left:0;top:0;width:480px;height:392px;background:var(--yellow);padding:32px 40px 0 232px;color:var(--white)}
.features-intro .label{color:var(--white);opacity:.85}
.features-intro h2{font-size:22px;font-weight:700;line-height:1.3;margin:12px 0 16px}
.features-intro p{font-size:10px;line-height:1.6;opacity:.9}
.features-intro .btn{margin-top:22px;background:var(--white);color:var(--ink);border-color:var(--white);padding:8px 14px;font-size:9px}
.feature-grid{left:520px;top:36px;width:450px;display:grid;grid-template-columns:1fr 1fr;gap:36px 30px}
.feature svg{width:26px;height:26px;display:block;margin-bottom:10px}
.feature h3{font-size:13px;font-weight:500;margin-bottom:8px}
.feature p{font-size:9.5px;line-height:1.6;color:var(--muted)}

/* stats */
.stats{top:712px;height:248px}
.stats-panel{left:232px;top:0;width:488px;height:248px;background:var(--blue);color:var(--white);display:flex;gap:50px;padding:64px 0 0 50px}
.stat strong{display:block;font-size:46px;font-weight:500;line-height:1}
.stat span{display:block;font-size:9.5px;line-height:1.6;max-width:140px;margin-top:12px;opacity:.9}
.stats-photo{left:720px;top:0;width:480px;height:248px;background:linear-gradient(135deg,#cfd6df,#6f8095 60%,#2d3543)}

/* services */
.services{top:980px;height:480px;text-align:center}
.services .label{margin-top:26px}
.services .h2{margin-top:8px;font-size:26px}
.service-photos{left:232px;top:120px;width:736px;display:grid;grid-template-columns:repeat(3,1fr);gap:8px}
.service-photos div{height:160px}
.service-cards{left:232px;top:280px;width:736px;display:grid;grid-template-columns:repeat(3,1fr);background:var(--white);box-shadow:0 8px 24px rgba(20,30,50,.08);text-align:left}
.service-card{padding:24px 22px;border-right:1px solid var(--line)}
.service-card:last-child{border:0}
.service-card .head{display:flex;align-items:center;gap:10px;margin-bottom:14px}
.service-card svg{width:26px;height:26px}
.service-card h3{font-size:13px;font-weight:500}
.service-card .more{display:block;margin-top:14px;font-size:9px;font-weight:500;letter-spacing:1px;color:var(--ink)}

/* trust */
.trust{top:1520px;height:580px;background:linear-gradient(90deg,var(--darker),#2a2c33 55%,#3a3d44);color:var(--white)}
.trust .label{left:232px;top:62px;color:var(--yellow)}
.trust h2{left:232px;top:80px;width:240px;font-size:21px;font-weight:700;line-height:1.3}
.trust .btn{left:232px;top:172px;color:var(--white);padding:8px 14px;font-size:9px}
.quote-mark{left:488px;top:70px;color:var(--blue);font-size:44px;font-weight:700;line-height:1}
.quote{left:488px;top:106px;width:480px;font-size:14px;line-height:1.6;color:#d9dbe0}
.quote-name{left:488px;top:192px;font-size:10px;letter-spacing:1px;font-weight:500}
.quote-role{left:488px;top:208px;font-size:9px;color:var(--muted)}
.stars{left:908px;top:214px;display:flex;gap:3px}
.arrows{left:1010px;top:74px;display:flex;gap:16px}
.trust-photos{left:232px;top:280px;width:520px;display:grid;grid-template-columns:repeat(3,1fr);gap:8px}
.trust-photos div{height:200px}
.trust-box{left:768px;top:290px;width:200px;height:180px;background:var(--blue);padding:34px 24px;text-align:center}
.trust-box p{font-size:10px;line-height:1.6}
.trust-box .btn{margin-top:16px;background:var(--white);color:var(--ink);border-color:var(--white);padding:7px 12px;font-size:8px}

/* cctv */
.cctv{top:2120px;height:268px}
.cctv .label{left:232px;top:22px}
.cctv h2{left:232px;top:40px;font-size:26px;line-height:1.25}
.cctv p{left:232px;top:116px;width:260px}
.bars{left:232px;top:166px;width:230px}
.bar{margin-bottom:14px}
.bar .row{display:flex;justify-content:space-between;font-size:9px;margin-bottom:5px}
.bar .track{height:3px;background:var(--line)}
.bar .fill{height:3px;background:var(--blue)}
.camera{left:520px;top:10px;width:320px;height:300px;background:radial-gradient(circle at 40% 45%,#f4f5f7,#c9ccd1 60%,#ffffff 75%);border-radius:20px;z-index:2}

/* consult band */
.consult{top:2388px;height:152px;background:var(--yellow)}
.consult-box{left:232px;top:0;width:228px;height:152px;background:var(--dark);color:var(--white);padding:44px 30px}
.consult-box span{display:block;font-size:11px;font-weight:500;letter-spacing:1px;line-height:1.5}
.consult-box strong{display:block;margin-top:8px;font-size:18px;color:var(--yellow);font-weight:500}
.badges{left:510px;top:56px;display:flex;gap:40px}
.badges div{width:54px;height:40px;border:2px solid rgba(255,255,255,.85);border-radius:4px}
.badges div:nth-child(odd){border-radius:50%;width:40px}

/* blog */
.blog{top:2540px;height:348px;text-align:center}
.blog .label{margin-top:24px}
.blog .h2{font-size:22px;line-height:1.3;margin-top:8px}
.posts{left:232px;top:128px;width:736px;display:grid;grid-template-columns:repeat(3,1fr);gap:14px;text-align:left}
.post .img{height:108px}
.post .body{padding:14px 0}
.post .meta{font-size:8.5px;color:var(--muted);margin-bottom:6px}
.post h3{font-size:12px;font-weight:500;line-height:1.4}
.post .more{display:block;margin-top:8px;font-size:9px;color:var(--blue);font-weight:500}

/* footer */
.site-footer{top:2888px;height:236px;background:var(--darker);color:#c5c8cf}
.contacts{left:232px;top:34px;width:736px;display:flex;justify-content:space-between}
.contact{display:flex;align-items:center;gap:10px;font-size:10px}
.contact svg{width:20px;height:20px}
.contact b{color:var(--white);font-weight:500}
.footer-rule{left:232px;top:84px;width:736px;height:1px;background:#2a2c33}
</style>
</head>
<body>

<section class="hero">
  <div class="abs hero-figure" role="img" aria-label="Technician in uniform giving an okay sign"></div>
  <h1 class="abs">We Offers Simple<br>Security System</h1>
  <div class="abs dots"><span></span><span></span></div>
</section>

<section class="features">
  <div class="abs features-intro">
    <div class="label">Why choose us</div>
    <h2>When you need better security installation</h2>
    <p>We plan, fit and look after alarm and camera systems for homes and businesses with care.</p>
    <span class="btn">Contact us</span>
  </div>
  <div class="abs feature-grid">
    <div class="feature">
      <svg viewBox="0 0 26 26" fill="none" stroke="#2f6be3" stroke-width="1.6"><rect x="3" y="4" width="20" height="14"/><path d="M9 22h8M13 18v4"/></svg>
      <h3>Reliable and Proven</h3>
      <p>Tested systems that keep working day and night, backed by years of steady local service.</p>
    </div>
    <div class="feature">
      <svg viewBox="0 0 26 26" fill="none" stroke="#2f6be3" stroke-width="1.6"><circle cx="13" cy="8" r="4"/><path d="M5 23c0-5 4-8 8-8s8 3 8 8"/></svg>
      <h3>Experts and Staff</h3>
      <p>Trained installers who explain each step and leave your site clean, safe and secure.</p>
    </div>
    <div class="feature">
      <svg viewBox="0 0 26 26" fill="none" stroke="#2f6be3" stroke-width="1.6"><rect x="3" y="6" width="20" height="14"/><circle cx="13" cy="13" r="3"/></svg>
      <h3>Affordable Rates</h3>
      <p>Clear pricing with no hidden costs, and plans that fit every home or business budget.</p>
    </div>
    <div class="feature">
      <svg viewBox="0 0 26 26" fill="none" stroke="#2f6be3" stroke-width="1.6"><path d="M4 14a9 9 0 0 1 18 0"/><rect x="3" y="14" width="4" height="6"/><rect x="19" y="14" width="4" height="6"/></svg>
      <h3>24/7/365 Support</h3>
      <p>Our team is ready to answer any call at any hour, every single day of the year.</p>
    </div>
  </div>
</section>

<section class="stats">
  <div class="abs stats-panel">
    <div class="stat"><strong>450<sup>+</sup></strong><span>Homes and offices protected by our systems this year</span></div>
    <div class="stat"><strong>875<sup>+</sup></strong><span>Cameras fitted and monitored across the region</span></div>
  </div>
  <div class="abs stats-photo" role="img" aria-label="Operator watching a wall of surveillance monitors"></div>
</section>

<section class="services">
  <div class="label">What we provide</div>
  <div class="h2">We Provide Awesome Expert<br>Security Service</div>
  <div class="abs service-photos">
    <div style="background:linear-gradient(135deg,#b9bec6,#5d6470)" role="img" aria-label="Security camera on a wall"></div>
    <div style="background:linear-gradient(135deg,#d7d9dd,#7d8390)" role="img" aria-label="Dome cameras on a ceiling"></div>
    <div style="background:linear-gradient(135deg,#c7a27a,#5b4a3a)" role="img" aria-label="Technician wiring a control panel"></div>
  </div>
  <div class="abs service-cards">
    <div class="service-card">
      <div class="head"><svg viewBox="0 0 26 26" fill="none" stroke="#2f6be3" stroke-width="1.6"><path d="M4 12l9-7 9 7v10H4z"/></svg><h3>Private Security</h3></div>
      <p class="small">Alarms and cameras planned around your home and family routine.</p>
      <span class="more">READ MORE</span>
    </div>
    <div class="service-card">
      <div class="head"><svg viewBox="0 0 26 26" fill="none" stroke="#2f6be3" stroke-width="1.6"><path d="M3 10l10-6 10 6M5 10v10M11 10v10M15 10v10M21 10v10M3 22h20"/></svg><h3>Banking Sector</h3></div>
      <p class="small">Layered access control and recording built for high value sites.</p>
      <span class="more">READ MORE</span>
    </div>
    <div class="service-card">
      <div class="head"><svg viewBox="0 0 26 26" fill="none" stroke="#2f6be3" stroke-width="1.6"><path d="M2 10l11-5 11 5-11 5z"/><path d="M7 13v5c3 2 9 2 12 0v-5"/></svg><h3>Education Institute</h3></div>
      <p class="small">Safe campuses with smart entry points and wide area coverage.</p>
      <span class="more">READ MORE</span>
    </div>
  </div>
</section>

<section class="trust">
  <div class="abs label">Our clients</div>
  <h2 class="abs">We are Trusted 15+<br>Countries Worldwide</h2>
  <span class="abs btn">View all</span>
  <div class="abs arrows">
    <svg width="22" height="12" viewBox="0 0 22 12" fill="none" stroke="#fff" stroke-width="1.4"><path d="M21 6H2M7 1L2 6l5 5"/></svg>
    <svg width="22" height="12" viewBox="0 0 22 12" fill="none" stroke="#fff" stroke-width="1.4"><path d="M1 6h19M15 1l5 5-5 5"/></svg>
  </div>
  <div class="abs quote-mark">“</div>
  <p class="abs quote">The Experts are installed &amp; maintain security system at my office and their security staff work great. They growing my answer &amp; security when I need Thanks for a great service.</p>
  <div class="abs quote-name">DAN MORELAND</div>
  <div class="abs quote-role">Office Manager</div>
  <div class="abs stars">
    <svg width="60" height="10" viewBox="0 0 60 10" fill="#dea63c"><path d="M5 0l1.5 3.2 3.5.4-2.6 2.3.8 3.5L5 7.6 1.8 9.4l.8-3.5L0 3.6l3.5-.4zM17 0l1.5 3.2 3.5.4-2.6 2.3.8 3.5L17 7.6l-3.2 1.8.8-3.5L12 3.6l3.5-.4zM29 0l1.5 3.2 3.5.4-2.6 2.3.8 3.5L29 7.6l-3.2 1.8.8-3.5L24 3.6l3.5-.4zM41 0l1.5 3.2 3.5.4-2.6 2.3.8 3.5L41 7.6l-3.2 1.8.8-3.5L36 3.6l3.5-.4zM53 0l1.5 3.2 3.5.4-2.6 2.3.8 3.5L53 7.6l-3.2 1.8.8-3.5L48 3.6l3.5-.4z"/></svg>
  </div>
  <div class="abs trust-photos">
    <div style="background:linear-gradient(160deg,#9aa2ad,#3d434c)" role="img" aria-label="Camera mounted on a building corner"></div>
    <div style="background:linear-gradient(160deg,#e9eaec,#9ea3ab)" role="img" aria-label="Bright office lobby with cameras"></div>
    <div style="background:linear-gradient(160deg,#b4bbc4,#4b525d)" role="img" aria-label="Warehouse interior under surveillance"></div>
  </div>
  <div class="abs trust-box">
    <p>Secure your properties in the best way now</p>
    <span class="btn">Contact us</span>
  </div>
</section>

<section class="cctv">
  <div class="abs label">Our products</div>
  <h2 class="abs h2">Latest CCTV Video<br>Cameras</h2>
  <p class="abs small">Sharp day and night recording with remote viewing from your phone and quick alerts.</p>
  <div class="abs bars">
    <div class="bar"><div class="row"><span>Product Maintenance</span><span>95%</span></div><div class="track"><div class="fill" style="width:95%"></div></div></div>
    <div class="bar"><div class="row"><span>Complete Solutions</span><span>85%</span></div><div class="track"><div class="fill" style="width:85%"></div></div></div>
    <div class="bar"><div class="row"><span>Service Warranty</span><span>90%</span></div><div class="track"><div class="fill" style="width:90%"></div></div></div>
  </div>
  <div class="abs camera" role="img" aria-label="White outdoor CCTV camera on a bracket"></div>
</section>

<section class="consult">
  <div class="abs consult-box">
    <span>GET FREE<br>CONSULTANCY OR</span>
    <strong>+1 (555) 010 4827</strong>
  </div>
  <div class="abs badges"><div></div><div></div><div></div><div></div><div></div></div>
</section>

<section class="blog">
  <div class="label">Latest news</div>
  <div class="h2">Get Leading Advice's on our<br>Security System</div>
  <div class="abs posts">
    <div class="post">
      <div class="img" style="background:linear-gradient(135deg,#c9d2dc,#5f6d7c)" role="img" aria-label="Installer fitting a camera indoors"></div>
      <div class="body"><div class="meta">12 March · Tips</div><h3>Quickly respond on your Device for Inspection</h3><span class="more">Read more</span></div>
    </div>
    <div class="post">
      <div class="img" style="background:linear-gradient(135deg,#dfe3e8,#7c8794)" role="img" aria-label="Team reviewing camera footage"></div>
      <div class="body"><div class="meta">08 March · News</div><h3>Latest Security technology for the Observation</h3><span class="more">Read more</span></div>
    </div>
    <div class="post">
      <div class="img" style="background:linear-gradient(135deg,#d3d7dc,#6a7380)" role="img" aria-label="Engineer checking an alarm panel"></div>
      <div class="body"><div class="meta">02 March · Guide</div><h3>Get The our best security Out Of Security Set</h3><span class="more">Read more</span></div>
    </div>
  </div>
</section>

<footer class="site-footer">
  <div class="abs contacts">
    <div class="contact"><svg viewBox="0 0 20 20" fill="none" stroke="#dea63c" stroke-width="1.5"><path d="M5 2l3 4-2 2c1 2 3 4 5 5l2-2 4 3-2 3C9 17 3 11 2 5z"/></svg><span><b>Call us</b><br>+1 (555) 010 4827</span></div>
    <div class="contact"><svg viewBox="0 0 20 20" fill="none" stroke="#dea63c" stroke-width="1.5"><path d="M10 18s6-6 6-10a6 6 0 0 0-12 0c0 4 6 10 6 10z"/><circle cx="10" cy="8" r="2"/></svg><span><b>Office address</b><br>48 Harlow Street, Eastfield</span></div>
    <div class="contact"><svg viewBox="0 0 20 20" fill="none" stroke="#dea63c" stroke-width="1.5"><rect x="2" y="4" width="16" height="12"/><path d="M2 5l8 6 8-6"/></svg><span><b>Email address</b><br>hello@sentrafield.com</span></div>
  </div>
  <div class="abs footer-rule"></div>
</footer>

</body>
</html>
```